Healthcare IT company looking for business card design

We develop IT systems for healthcare that significantly reduces cost and improves quality.

We want a business card design that is professional and clean, and using the colors in our logo.

Target Market(s)

Doctors and decision makers in the healthcare industry

Industry/Entity Type

Healthcare

Contact Information for Business Card

It should include
Name and title, address, telephone

Tobias Vrenholt, CEO
+46 712 418257
tobias@kelvaro.se

Font styles to use
Serif

Colors
0355a3
ed282f

Requirements
Must have
• Clean design
• Professional feel
Nice to have
• N/A
Should not have
• N/A

```html
<!DOCTYPE html>
<html lang="en">
<head>
<meta charset="utf-8">
<title>Kelvaro business card</title>
<link href="https://fonts.googleapis.com/css2?family=Source+Sans+3:wght@400;600;700&display=swap" rel="stylesheet">
<style>
  :root {
    --brand-blue: #1561ae;
    --brand-red: #ed282f;
    --ink: #111111;
    --muted: #6b6b6b;
    --paper: #ffffff;
    --backdrop: #e7e2da;
  }
  html, body {
    margin: 0;
    padding: 0;
    width: 1200px;
    height: 1200px;
    overflow: hidden;
    background: var(--backdrop);
    font-family: "Source Sans 3", sans-serif;
  }
  .stage { position: relative; width: 1200px; height: 1200px; }
  .card {
    position: absolute;
    left: 185px;
    width: 830px;
    border-radius: 28px;
    box-shadow: 0 6px 18px rgba(0,0,0,0.18);
    overflow: hidden;
  }
  .card--front { top: 48px; height: 542px; background: var(--paper); }
  .card--back { top: 608px; height: 544px; background: var(--brand-blue); }

  .wordmark {
    position: absolute;
    display: flex;
    align-items: center;
    font-weight: 700;
    letter-spacing: -0.5px;
    line-height: 1;
  }
  .wordmark__dot { border-radius: 50%; background: var(--brand-red); flex: none; }
  .card--front .wordmark {
    right: 56px;
    top: 52px;
    font-size: 100px;
    color: var(--brand-blue);
    gap: 14px;
  }
  .card--front .wordmark__dot { width: 26px; height: 26px; }
  .card--back .wordmark {
    left: 0; right: 0; top: 50%;
    transform: translateY(-52%);
    justify-content: center;
    font-size: 190px;
    color: var(--paper);
    gap: 24px;
  }
  .card--back .wordmark__dot { width: 46px; height: 46px; }

  .contact {
    position: absolute;
    left: 44px;
    top: 206px;
    color: var(--ink);
  }
  .contact__name { margin: 0; font-size: 38px; font-weight: 600; line-height: 1.1; }
  .contact__title { margin: 2px 0 0; font-size: 25px; font-weight: 600; color: var(--muted); letter-spacing: 0.5px; }
  .contact__address { margin: 20px 0 0; font-size: 25px; line-height: 34px; }
  .contact__lines { margin: 12px 0 0; font-size: 25px; line-height: 34px; }
  .contact__label { color: var(--brand-red); display: inline-block; width: 33px; }
  .contact__gap { display: inline-block; width: 16px; }
  .contact__web { margin: 10px 0 0; font-size: 31px; color: var(--brand-blue); }
  .contact__web strong { font-weight: 700; }
  .contact__web .tld { color: var(--brand-red); }
</style>
</head>
<body>
<main class="stage">
  <section class="card card--front">
    <div class="wordmark"><span>Kelvaro</span><span class="wordmark__dot"></span></div>
    <div class="contact">
      <h1 class="contact__name">Tobias Vrenholt</h1>
      <p class="contact__title">CEO</p>
      <p class="contact__address">Address, Street<br>City, State Zip</p>
      <p class="contact__lines">
        <span class="contact__label">t:</span>+46 712 418257<span class="contact__gap"></span><span class="contact__label">c:</span>+46 712 418257<br>
        <span class="contact__label">e:</span>tobias@kelvaro.se
      </p>
      <p class="contact__web">www.<strong>kelvaro</strong><span class="tld">.se</span></p>
    </div>
  </section>
  <section class="card card--back">
    <div class="wordmark"><span>Kelvaro</span><span class="wordmark__dot"></span></div>
  </section>
</main>
</body>
</html>
```